Upcoming lecture sponsored by a church on an important topic

We have a Reformation The Speech coming up at the end of October on the topic of law and gospel. I thought it might be cool to use a flyer that looks like it was from that day and age. Picture what Conrad Velmer would advertise things on kind of an old church/reformation type format. It will be sponsored by our church, and we have a paragraph or two to describe the lecture that would be included on the flyer. We would also want it formatted so that it could be printed on postcards and mailed to churches and individuals.

The flyer should have the following paragraph...

The distinction between the law and the gospel is the most important distinction in the Christian faith. Conrad Velmer: “Distinguishing between the law and the gospel is the highest art in Christendom, one who every person who values the name Christian ought to recognize, know, and possess.” The distinction between the law and the gospel is of great comfort for the child of God. “For the law was given by Moses, but grace and truth came by Jesus Christ” (John 1:17). For these reasons, the distinction between the law and the gospel is the most heavily assaulted doctrine in the Christian faith. This Reformation Day, join us for an explanation and defense of the great distinction between God’s good law and God’s glorious gospel.

And the flyer should have the following information...

Topic: The Steady Word and the Bright Promise
Date and Time: Tuesday, October 31, 2023 at 7:30pm
Host: Harrow Creek Fellowship Church
Speaker: Rev. Gerald Voskuil
Venue: The Marlow Hall, 5172 Brenton Avenue, Hudsonville, MI 49318
Format: Lecture followed by Q&A and refreshments

00AB8E
00BBA5
67D7C9
C6EFE9
E9F9F6

• The color scheme that I would like to have is a teal color (the same color as found at www.brackenhollowchapel.com

```html
<!DOCTYPE html>
<html lang="en">
<head>
<meta charset="utf-8">
<title>The Steady Word and the Bright Promise — Reformation Day Lecture</title>
<link href="https://fonts.googleapis.com/css2?family=Oswald:wght@600;700&family=Great+Vibes&family=Roboto:wght@400;500;700&display=swap" rel="stylesheet">
<style>
  :root{
    --page-bg:#e6e7e9;
    --sky-top:#7fc4f2;
    --sky-mid:#3fa6ea;
    --sky-deep:#1e86d6;
    --band:#1a6fb8;
    --white:#ffffff;
    --paper:#f7f9fb;
    --ink-soft:#eaf5fd;
    --photo-a:#d9d2c6;
    --photo-b:#8a6a4c;
    --photo-c:#3e2b1f;
  }
  *{margin:0;padding:0;box-sizing:border-box}
  html,body{width:1200px;height:2168px;overflow:hidden}
  body{background:var(--page-bg);font-family:'Roboto',sans-serif;position:relative}

  .flyer{
    position:absolute;left:50px;top:306px;width:1100px;height:1556px;
    background:linear-gradient(180deg,var(--sky-top) 0%,var(--sky-mid) 45%,var(--sky-deep) 100%);
    overflow:hidden;box-shadow:0 6px 24px rgba(0,0,0,.18);
    color:var(--white);text-align:center;
  }
  .flyer__photo{
    position:absolute;left:0;top:0;width:100%;height:560px;
    background:linear-gradient(135deg,var(--photo-a) 0%,var(--photo-b) 55%,var(--photo-c) 100%);
  }
  .flyer__tear-top,.flyer__tear-bottom{position:absolute;left:0;width:100%}
  .flyer__tear-top{top:470px;height:120px}
  .flyer__tear-bottom{bottom:0;height:110px}

  .title{position:absolute;left:0;right:0;top:600px}
  .title__caps{
    font-family:'Oswald',sans-serif;font-weight:700;font-size:92px;letter-spacing:1px;
    line-height:1;text-transform:uppercase;text-shadow:0 3px 6px rgba(0,40,90,.25);
  }
  .title__script{
    font-family:'Great Vibes',cursive;font-size:118px;line-height:1.05;margin-top:4px;
    text-shadow:0 3px 6px rgba(0,40,90,.25);
  }
  .date{
    position:absolute;left:0;right:0;top:858px;
    font-family:'Roboto',sans-serif;font-weight:500;font-size:44px;
  }
  .credits{
    position:absolute;left:190px;right:190px;top:930px;height:52px;
    background:var(--band);display:flex;align-items:center;justify-content:center;gap:22px;
    font-size:24px;font-weight:700;
  }
  .credits__dot{width:6px;height:6px;border-radius:50%;background:var(--white)}
  .description{
    position:absolute;left:170px;right:170px;top:1010px;
    font-size:20px;line-height:1.45;color:var(--ink-soft);
  }
  .description p+p{margin-top:18px}
  .venue{position:absolute;left:0;right:0;top:1345px;font-size:20px;line-height:1.45}
  .venue__label{font-weight:700;font-size:24px;margin-bottom:4px}
</style>
</head>
<body>
  <article class="flyer">
    <div class="flyer__photo" role="img" aria-label="Photograph of folded hands resting on an open Bible with a wooden rosary"></div>
    <svg class="flyer__tear-top" viewBox="0 0 1100 120" preserveAspectRatio="none" aria-hidden="true">
      <path fill="#f7f9fb" d="M0 60 L60 48 L110 70 L170 52 L240 78 L300 58 L360 74 L430 50 L500 72 L560 56 L640 80 L700 60 L770 76 L840 54 L910 72 L980 58 L1040 74 L1100 60 L1100 120 L0 120 Z"/>
      <path fill="#7fc4f2" d="M0 82 L70 72 L130 90 L200 76 L270 96 L340 80 L410 94 L480 74 L550 92 L620 78 L690 98 L760 82 L830 94 L900 76 L970 92 L1040 80 L1100 90 L1100 120 L0 120 Z"/>
    </svg>

    <header class="title">
      <h1 class="title__caps">The Steady Word and</h1>
      <p class="title__script">The Bright Promise</p>
    </header>

    <p class="date">Tuesday, October 31, 2023 at 7.30 pm</p>

    <div class="credits">
      <span>Host: Harrow Creek Fellowship Church</span>
      <span class="credits__dot"></span>
      <span>Speaker: Rev. Gerald Voskuil</span>
    </div>

    <section class="description">
      <p>The distinction between the law and the gospel is the most important distinction in the Christian faith. Conrad Velmer: “Distinguishing between the law and the gospel is the highest art in Christendom, one who every person who values the name Christian ought to recognize, know, and possess.” The distinction between the law and the gospel is of great comfort for the child of God.</p>
      <p>“For the law was given by Moses, but grace and truth came by Jesus Christ” (John 1:17). For these reasons, the distinction between the law and the gospel is the most heavily assaulted doctrine in the Christian faith. This Reformation Day, join us for an explanation and defense of the great distinction between God’s good law and God’s glorious gospel.</p>
    </section>

    <footer class="venue">
      <p class="venue__label">Venue:</p>
      <p>The Marlow Hall, 5172 Brenton Avenue, Hudsonville, MI 49318</p>
      <p>Format: Lecture followed by Q&amp;A and refreshments</p>
    </footer>

    <svg class="flyer__tear-bottom" viewBox="0 0 1100 110" preserveAspectRatio="none" aria-hidden="true">
      <path fill="#f7f9fb" d="M0 50 L70 62 L140 44 L210 66 L280 48 L350 70 L420 52 L490 68 L560 46 L630 64 L700 50 L770 70 L840 52 L910 66 L980 48 L1050 62 L1100 52 L1100 110 L0 110 Z"/>
    </svg>
  </article>
</body>
</html>
```